Property Investment eBook Cover

I am a long established Australian property investment adviser, analyst and consultant who is now in semi-retired mode and have re-branded to reflect a more casual and personal approach to advising my property investor clients. I am writing a 'revised edition' to a book written in partnership with my father 20 years ago and need an eBook Cover for this new edition. The eBook will be uploaded to all the regular Australian providers (Tarvo Reader, Quillet Epage, Zeni, Pagemarsh)

The 3 key elements in the book cover are:

Title: The Riches Engine of Land. The word 'Property' should be larger and more prominent. eg "The Wealth Power of" could be 1/3 the size of "Property" - with both justified left

Edition: Sydney 2021. "Sydney 2021" should be the focus and dominant imagery of the eBook cover and more prominent than the Title or Author

Author: Glen Markby, The Housing Numbers Guide. The word "Author" should not appear. "The Housing Numbers Guide" should appear underneath Glen Markby and justified to Glen Markby, therefore a smaller font.

The cover should be simple, but eye-catching. No property images, more of an abstract background, than a background with an image. Our preferred colour palette is more blues/greens. Prefer SerifFonts

Copy of book published 20 years ago attached for reference only

```html
<!DOCTYPE html>
<html lang="en">
<head>
<meta charset="utf-8">
<title>The Riches Engine of Land — Glen Markby</title>
<link rel="stylesheet" href="https://fonts.googleapis.com/css2?family=Bodoni+Moda:opsz,wght@6..96,600;6..96,700&family=Roboto+Condensed:wght@500&display=swap">
<style>
  :root {
    --page-bg: #cbdadc;
    --cover-base: #cfd4db;
    --wash-green: #c3cbb9;
    --wash-light: #dde1e7;
    --frame-band: #c4cbbd;
    --frame-inner: #d3d8de;
    --ink: #151515;
    --badge-red: #a0131f;
    --badge-text: #f1d9dc;
  }
  * { margin: 0; padding: 0; box-sizing: border-box; }
  html, body {
    width: 1191px;
    height: 1200px;
    overflow: hidden;
    background: var(--page-bg);
  }
  .cover {
    position: absolute;
    left: 315px;
    top: 180px;
    width: 560px;
    height: 815px;
    overflow: hidden;
    background: var(--cover-base);
  }
  .cover__wash {
    position: absolute;
    inset: 0;
    background:
      radial-gradient(ellipse 45% 30% at 80% 35%, var(--wash-green) 0%, transparent 70%),
      radial-gradient(ellipse 40% 25% at 25% 8%, var(--wash-green) 0%, transparent 70%),
      radial-gradient(ellipse 40% 30% at 15% 88%, var(--wash-green) 0%, transparent 70%),
      linear-gradient(160deg, var(--wash-light) 0%, var(--cover-base) 60%, #c9ced6 100%);
  }
  .cover__frame {
    position: absolute;
    left: 93px;
    top: 152px;
    width: 363px;
    height: 528px;
    border: 17px solid var(--frame-band);
    background: var(--frame-inner);
    opacity: 0.85;
  }
  .edition-badge {
    position: absolute;
    right: 0;
    top: 0;
    width: 150px;
    height: 130px;
  }
  .title {
    position: absolute;
    left: 0;
    width: 100%;
    text-align: center;
    font-family: "Bodoni Moda", "Didot", serif;
    font-weight: 700;
    color: var(--ink);
    line-height: 1;
  }
  .title__line--the { top: 232px; font-size: 50px; }
  .title__line--riches { top: 318px; font-size: 50px; letter-spacing: -1px; }
  .title__line--of { top: 400px; font-size: 50px; }
  .title__line--land { top: 500px; font-size: 50px; letter-spacing: 4px; }
  .author {
    position: absolute;
    left: 0;
    top: 694px;
    width: 100%;
    text-align: center;
    font-family: "Bodoni Moda", "Didot", serif;
    font-weight: 700;
    color: var(--ink);
  }
  .author__name { font-size: 27px; line-height: 1; letter-spacing: 0.5px; }
  .author__role { font-size: 15px; line-height: 1; margin-top: 6px; }
</style>
</head>
<body>
  <main class="cover">
    <div class="cover__wash" role="img" aria-label="Abstract pale green and grey watercolour wash background"></div>
    <div class="cover__frame"></div>

    <svg class="edition-badge" viewBox="0 0 150 130" aria-label="Sydney 2021 edition">
      <circle cx="150" cy="-20" r="148" fill="var(--badge-red)"/>
      <g font-family="'Roboto Condensed', sans-serif" font-weight="500" fill="var(--badge-text)" font-size="24" letter-spacing="1">
        <text x="0" y="0" transform="translate(52 20) rotate(40)">Sydney</text>
        <text x="0" y="0" transform="translate(40 42) rotate(40)">2021</text>
      </g>
    </svg>

    <h1>
      <span class="title title__line--the">The</span>
      <span class="title title__line--riches">Riches Engine</span>
      <span class="title title__line--of">of</span>
      <span class="title title__line--land">LAND</span>
    </h1>

    <div class="author">
      <p class="author__name">Glen Markby</p>
      <p class="author__role">The Housing Numbers Guide</p>
    </div>
  </main>
</body>
</html>
```